Promotional Flyer/Email Design - Cabling services for Broadcast and Audio Visual

We need a promotional flyer/email design to help launch our company, Velcor Lane. We provide cabling services for Broadcast Television and Audio Visual systems. Recent projects include major television events such as the Harrowmere Racquet Classic and Audio Visual/Entertainment systems for wealthy clients in their homes and on-board super yachts.

The flyer will be printed as single sided A5 and also be sent out in the body of a promotional email. It should feature the company logo along with a complementary colour scheme. It should have a clean finish with images that show the type of work we do (cabling and equipment installation) or the setting for these systems (tv studio, super yacht, cinema room, meeting room with projector etc.)

Services we offer are:

Broadcast/AV system design
On-site installation
Rack building
Pre-fabricated cable looms
Fibre optic installation

About the company:

Velcor Lane provide cabling services for Broadcast Television and Audio Visual systems. With over 15 years experience working in these industries we can help with every aspect of design, project managment, installation and maintenance. Our projects range from fibre optic cabling at major sports events to installing and commisioning bespoke control systems on some of the worlds largest super yachts.

Contact details:

To get a quote or discuss your project contact us now
Telephone: TBC
Email: info@velcor-lane.com
Website: www.velcor-lane.com
Address: TBC

Other information:

The company is based in London, UK. Our projects often take place in other countries with work taking place accross Europe and beyond.

We have a London based workshop for rack building and cable pre-fabrication.

Our website is www.velcor-lane.com

Images:

Images attached can be editted for use on the flyer or have ideas taken from them. Only the company logo is required to feature on the final design.

Target Market(s)

Business to business

Industry/Entity Type

It Company

Font styles to use
Sans Serif

Requirements
Must have
• Company logo
• List of services
• Contact details
Nice to have
• Image of cabling, home cinema room, super yacht, luxury home, outside broadcast truck, fibre optic equipment or cabling.

```html
<!DOCTYPE html>
<html lang="en">
<head>
<meta charset="utf-8">
<title>Velcor Lane – Cabling for Broadcast and AV</title>
<link rel="stylesheet" href="https://fonts.googleapis.com/css2?family=Montserrat:wght@400;500;600;700;800&display=swap">
<style>
  :root {
    --page: #e4e4e6;
    --charcoal: #2e2d30;
    --blue: #2a8bea;
    --red: #e01048;
    --yellow: #f5b400;
    --white: #ffffff;
    --paper: #f4f4f5;
    --grey-mark: #8e8e90;
    --ink: #2e2d30;
    --muted: #6d6d70;
  }
  * { box-sizing: border-box; margin: 0; padding: 0; }
  html, body { width: 1200px; height: 1200px; overflow: hidden; }
  body {
    background: var(--page);
    font-family: "Montserrat", sans-serif;
    position: relative;
  }
  .flyer {
    position: absolute;
    left: 197px; top: 30px;
    width: 806px; height: 1140px;
    overflow: hidden;
    background: var(--charcoal);
    color: var(--white);
  }
  .flyer-shapes { position: absolute; inset: 0; }
  .hero-badge {
    position: absolute;
    left: -40px; top: 20px;
    width: 420px; height: 420px;
    border-radius: 50%;
    background: var(--blue);
    padding: 110px 40px 0 110px;
  }
  .hero-badge .lead {
    font-size: 27px; font-weight: 500; line-height: 1.22;
  }
  .hero-badge .punch {
    margin-top: 22px;
    font-size: 27px; font-weight: 800;
  }
  .hero-badge .note { font-size: 11px; font-weight: 400; opacity: .9; }
  .about {
    position: absolute; left: 440px; top: 388px; width: 340px;
    font-size: 13px; line-height: 1.4;
  }
  .services { position: absolute; left: 440px; top: 500px; width: 340px; }
  .services h2 {
    font-size: 20px; font-weight: 500; letter-spacing: .5px;
    padding-bottom: 6px; border-bottom: 2px solid var(--white);
    display: inline-block;
  }
  .services ul { list-style: none; margin-top: 20px; }
  .services li {
    display: flex; align-items: center; gap: 18px;
    font-size: 16px; font-weight: 600; height: 42px;
  }
  .services svg { width: 26px; height: 26px; flex: none; }
  .quote-mark {
    position: absolute; left: 70px; top: 540px;
    font-size: 170px; font-weight: 800; line-height: 1;
    color: var(--grey-mark);
  }
  .headline {
    position: absolute; left: 70px; top: 640px; width: 360px;
    color: var(--yellow);
    font-size: 37px; font-weight: 800; line-height: 1.12;
  }
  .projects {
    position: absolute; left: 70px; top: 815px; width: 360px;
    font-size: 13px; line-height: 1.35;
  }
  .brand {
    position: absolute; left: 70px; top: 1030px; color: var(--ink);
  }
  .brand-name {
    display: flex; align-items: center; gap: 10px;
    font-size: 32px; font-weight: 700; letter-spacing: -.5px;
  }
  .brand-name .dot {
    width: 22px; height: 22px; border-radius: 50%; background: var(--red);
  }
  .brand address {
    font-style: normal; font-size: 14px; color: var(--muted); margin-top: 8px;
  }
  .contact {
    position: absolute; left: 500px; top: 950px; width: 280px; color: var(--ink);
  }
  .contact h3 { font-size: 28px; font-weight: 800; line-height: 1; }
  .contact .sub {
    font-size: 11px; font-weight: 500; letter-spacing: .5px;
    padding-bottom: 8px; border-bottom: 1px solid #9a9a9d; display: inline-block;
    margin-top: 4px;
  }
  .contact .phone {
    display: flex; align-items: center; gap: 8px;
    color: var(--red); font-size: 30px; font-weight: 600; margin-top: 10px;
  }
  .contact .line {
    display: flex; align-items: center; gap: 8px;
    font-size: 16px; font-weight: 500; margin-top: 4px;
  }
  .contact svg { flex: none; }
</style>
</head>
<body>
<article class="flyer">
  <svg class="flyer-shapes" viewBox="0 0 806 1140" preserveAspectRatio="none">
    <defs>
      <linearGradient id="venueTone" x1="0" y1="0" x2="1" y2="1">
        <stop offset="0" stop-color="#6f8a4e"/>
        <stop offset=".5" stop-color="#4f6a45"/>
        <stop offset="1" stop-color="#3e5a3a"/>
      </linearGradient>
    </defs>
    <rect class="hero-photo" x="0" y="0" width="806" height="640" fill="url(#venueTone)" role="img" aria-label="Aerial photograph of the Harrowmere Racquet Classic stadium and grass courts"/>
    <path class="wave-red" d="M0,530 C240,640 560,560 806,270 L806,1140 L0,1140Z" fill="var(--red)"/>
    <path class="wave-dark" d="M0,560 C250,670 580,590 806,305 L806,1140 L0,1140Z" fill="var(--charcoal)"/>
    <path class="footer-blue" d="M380,1140 C520,980 650,880 806,900 L806,1140Z" fill="var(--blue)"/>
    <path class="footer-paper" d="M0,1140 L0,1010 C250,990 540,880 806,918 L806,1140Z" fill="var(--paper)"/>
  </svg>

  <div class="hero-badge">
    <p class="lead">Broadcasting Harrowmere was equally thrilling as playing Harrowmere.</p>
    <p class="punch">And we delievered.</p>
    <p class="note">*as cabling partners for broadcast television</p>
  </div>

  <p class="about">Velcor Lane provide cabling services for Broadcast Television and Audio Visual systems. With over 15 years experience working in these industries we can help with every aspect of design, project managment, installation and maintenance.</p>

  <section class="services">
    <h2>OUR SERVICES</h2>
    <ul>
      <li><svg viewBox="0 0 26 26" fill="none" stroke="#fff" stroke-width="1.6"><path d="M13 12 L8 24 M13 12 L18 24 M10 19 H16"/><circle cx="13" cy="10" r="2"/><path d="M8 6 a7 7 0 0 1 10 0 M5 3 a11 11 0 0 1 16 0"/></svg>Broadcast/ AV System Design</li>
      <li><svg viewBox="0 0 26 26" fill="#fff"><circle cx="13" cy="11" r="6"/><circle cx="13" cy="11" r="2.5" fill="var(--charcoal)"/><path d="M3 20 v4 h20 v-4" fill="none" stroke="#fff" stroke-width="1.6"/></svg>On-site Installation</li>
      <li><svg viewBox="0 0 26 26" fill="#fff"><rect x="2" y="4" width="22" height="5"/><rect x="2" y="11" width="22" height="5"/><rect x="2" y="18" width="22" height="5"/></svg>Rack Building</li>
      <li><svg viewBox="0 0 26 26" fill="none" stroke="#fff" stroke-width="1.6"><rect x="4" y="3" width="14" height="20"/><path d="M4 9 L18 3 M4 15 L18 9 M4 21 L18 15 M18 20 q6 0 5 -6"/></svg>Pre-fabricated Cable Looms</li>
      <li><svg viewBox="0 0 26 26" fill="none" stroke="#fff" stroke-width="1.6"><path d="M13 25 V12 M13 12 L5 5 M13 12 L21 5 M13 12 L9 2 M13 12 L17 2"/></svg>Fibre optic installation</li>
    </ul>
  </section>

  <div class="quote-mark" aria-hidden="true">“</div>
  <h1 class="headline">Making the connections that digital innovation demands</h1>
  <p class="projects">Our projects range from fibre optic cabling at major sports events to installing and commisioning bespoke control systems on some of the worlds largest super yachts. The company based in London has executed projects successfully across Europe.</p>

  <div class="brand">
    <div class="brand-name"><span class="dot"></span>Velcor Lane</div>
    <address>45 Kestrel Yard, London, UK E2 7QB</address>
  </div>

  <div class="contact">
    <h3>GET A QUOTE</h3>
    <p class="sub">FEEL FREE TO CONTACT US.</p>
    <p class="phone"><svg width="24" height="24" viewBox="0 0 24 24" fill="var(--red)"><path d="M6.6 10.8a15 15 0 0 0 6.6 6.6l2.2-2.2c.3-.3.7-.4 1-.2 1.1.4 2.3.6 3.6.6.6 0 1 .4 1 1V20c0 .6-.4 1-1 1A17 17 0 0 1 3 4c0-.6.4-1 1-1h3.5c.6 0 1 .4 1 1 0 1.3.2 2.5.6 3.6.1.3 0 .7-.2 1z"/></svg>01632 960-4821</p>
    <p class="line"><svg width="16" height="12" viewBox="0 0 16 12" fill="var(--ink)"><path d="M0 0h16v12H0z M1 1l7 5 7-5" stroke="#fff" stroke-width="1"/></svg>info@velcor-lane.com</p>
    <p class="line"><svg width="16" height="14" viewBox="0 0 16 14" fill="var(--ink)"><path d="M8 0L0 7h2v7h4V9h4v5h4V7h2z"/></svg>www.velcor-lane.com</p>
  </div>
</article>
</body>
</html>
```